Help me design my in store poster to promote our Loan product!

We need a design for a 2 X 3 poster inside our stores to promote our installment loan product. We are called Dorn's Check Cashing, but offer loans inside our stores. We are open to a new logo for Dorn's Loans, and open to any new exciting colors to stand out in the store. We provide short term monthly installment loans, we have monthly payments from 3 - 12 months. Our loans range from $100 - $1,400 with low interest. We ask for ID, consistent source of income, and credit check. We help build credit, and it is fast and easy. We want it to be simple and clean to get people's attention when they are inside our stores. Please help!

UPDATE: The design will be for a 2 X 7 poster now. Less words.

Font styles to use
Other font styles liked:
• Rounded corners with the font

Requirements
Must have
• Bold colors, the words: loans, cash, $100 - $1,400, monthly payments, credit building, quick.
Nice to have
• A new logo, the Dorn's Check Cashing logo added as reference

UPDATE: If we can add a quick slogan : FAST CASH NOW or HELP IS HERE or YOUR CASH IS HERE or LOANS FOR LIVING or LOANS FOR LIFE

A DORN'S FINANCE LOGO that looks similar to the GALEWING logo I attached.

```html
<!DOCTYPE html>
<html lang="en">
<head>
<meta charset="utf-8">
<title>Dorn's Loans – Cash Loans Banner</title>
<link href="https://fonts.googleapis.com/css2?family=Anton&family=Oswald:wght@500;600&family=Russo+One&display=swap" rel="stylesheet">
<style>
  :root {
    --stage: #e9eaec;
    --navy: #0b2f7a;
    --royal: #0a48a8;
    --sky: #7ea9d6;
    --sky-bright: #6cb4ff;
    --ink: #1b1b1b;
    --white: #ffffff;
    --red: #e0141a;
    --red-dark: #a00b10;
    --rule: #8fb0d8;
  }
  * { margin: 0; padding: 0; box-sizing: border-box; }
  html, body { width: 1200px; height: 975px; overflow: hidden; background: var(--stage); }
  .canvas { position: relative; width: 1200px; height: 975px; }
  .banner {
    position: absolute; left: 465px; top: 18px;
    width: 270px; height: 940px;
    box-shadow: 0 6px 18px rgba(0,0,0,.25);
  }
  .banner-bg { position: absolute; inset: 0; }
  .headline {
    position: absolute; left: 0; width: 100%; top: 22px;
    text-align: center;
    font-family: "Anton", sans-serif;
    font-size: 108px; line-height: 106px; letter-spacing: 1px;
    background: linear-gradient(180deg, #ffffff 0%, #f2f2f2 35%, #a9a9ad 52%, #ffffff 68%, #cfcfd3 100%);
    -webkit-background-clip: text; background-clip: text; color: transparent;
    filter: drop-shadow(3px 4px 0 #06205a);
  }
  .offer {
    position: absolute; left: 16px; top: 271px; width: 238px; height: 178px;
  }
  .offer-text {
    position: absolute; inset: 0; padding-top: 12px;
    text-align: center; font-family: "Oswald", sans-serif; font-weight: 500;
    color: var(--white);
  }
  .offer-lead { font-size: 20px; line-height: 24px; letter-spacing: .3px; }
  .offer-range { font-family: "Anton", sans-serif; font-size: 38px; line-height: 46px; color: var(--sky-bright); }
  .offer-terms { font-size: 21px; line-height: 23px; margin-top: 2px; }
  .benefits {
    position: absolute; left: 22px; width: 226px; top: 470px;
    font-family: "Russo One", sans-serif; text-align: center; text-transform: uppercase;
  }
  .benefit { font-size: 27px; line-height: 28px; padding: 6px 0 9px; }
  .benefit + .benefit { border-top: 1px solid var(--rule); }
  .benefit--primary { color: var(--royal); }
  .benefit--soft { color: var(--sky); }
  .benefit--dark { color: var(--ink); font-size: 25px; }
  .brand {
    position: absolute; left: 22px; width: 226px; top: 708px; height: 96px;
    display: flex; align-items: center; justify-content: center; gap: 10px;
    font-family: "Russo One", sans-serif; font-size: 30px; color: var(--royal);
  }
  .brand-dot { width: 22px; height: 22px; border-radius: 50%; background: var(--royal); flex: none; }
  .cta { position: absolute; left: 31px; top: 840px; width: 208px; height: 80px; }
  .cta-text {
    position: absolute; inset: 0; padding-top: 9px; text-align: center;
    font-family: "Russo One", sans-serif; font-size: 27px; line-height: 26px;
    color: var(--white); text-shadow: 1px 2px 0 rgba(0,0,0,.35);
  }
</style>
</head>
<body>
<main class="canvas">
  <article class="banner">
    <svg class="banner-bg" width="270" height="940" viewBox="0 0 270 940" aria-hidden="true">
      <defs>
        <linearGradient id="cta-fill" x1="0" y1="0" x2="0" y2="1">
          <stop offset="0" stop-color="#ff2a2a"/>
          <stop offset="1" stop-color="#b00a0f"/>
        </linearGradient>
      </defs>
      <rect width="270" height="940" fill="#ffffff"/>
      <polygon points="0,0 270,0 270,440 0,440" fill="#7ea9d6"/>
      <polygon points="0,0 270,0 270,240 135,300 0,350" fill="#0a48a8"/>
      <polygon points="150,0 270,0 270,215 230,238" fill="#0b2f7a"/>
      <rect x="0" y="440" width="270" height="500" fill="#ffffff"/>
      <rect x="1" y="1" width="268" height="938" fill="none" stroke="#8fb0d8" stroke-width="2"/>
    </svg>

    <h1 class="headline">CASH<br>LOANS</h1>

    <section class="offer">
      <svg width="238" height="178" viewBox="0 0 238 178" aria-hidden="true" style="position:absolute;inset:0">
        <defs>
          <linearGradient id="offer-fill" x1="0" y1="0" x2="0" y2="1">
            <stop offset="0" stop-color="#4a4a4a"/>
            <stop offset="0.5" stop-color="#1e1e1e"/>
            <stop offset="1" stop-color="#0d0d0d"/>
          </linearGradient>
        </defs>
        <path d="M10,1 H228 Q237,1 237,10 V140 L119,177 L1,140 V10 Q1,1 10,1 Z" fill="url(#offer-fill)" stroke="#d8d8d8" stroke-width="1.5"/>
      </svg>
      <div class="offer-text">
        <p class="offer-lead">LOANS RANGE FROM</p>
        <p class="offer-range">$100 - $1,400</p>
        <p class="offer-terms">WITH<br>LOW INTEREST</p>
      </div>
    </section>

    <ul class="benefits" style="list-style:none">
      <li class="benefit benefit--primary">Monthly<br>Payments</li>
      <li class="benefit benefit--soft">Credit<br>Building</li>
      <li class="benefit benefit--dark">Fast &amp; Easy</li>
    </ul>

    <div class="brand"><span class="brand-dot"></span><span>DORN'S LOANS</span></div>

    <a class="cta">
      <svg width="208" height="80" viewBox="0 0 208 80" aria-hidden="true" style="position:absolute;inset:0">
        <path d="M4,0 H204 Q208,0 208,4 V62 L104,80 L0,62 V4 Q0,0 4,0 Z" fill="url(#cta-fill)"/>
      </svg>
      <span class="cta-text">APPLY<br>TODAY!</span>
    </a>
  </article>
</main>
</body>
</html>
```